Corvanta Energy LNG as Marine Fuel Slides Design

Slides template inspired by and using the attached Corvanta Energy logo. We are developing LNG as marine fuel facilities and bunkering vessels to supply the fuel to the marine industry. Designs should use the Corvanta Energy logo colors and be consistent with our vision of providing environmentally cleaner fuel supply. Our selected logo was 1A in the attached files, as shown on the business card template also attached.

Target Market(s)

Marine Industry (Shipping, container vessels, crude carriers, cargo / transportation vessels, etc.)

Requirements
Must have
• Clean / green energy theme
Compatibility with submitted logo and logo color scheme
Font headers that work well with the logo font
Nice to have
• Marine / Maritime theme
relevance to Gulf Coast Region
Should not have
• Dark colors

```html
<!DOCTYPE html>
<html lang="en">
<head>
<meta charset="utf-8">
<title>Corvanta Energy – Slide Set</title>
<link href="https://fonts.googleapis.com/css2?family=Open+Sans:wght@400;600;700&display=swap" rel="stylesheet">
<style>
  :root {
    --green: #70b244;
    --white: #ffffff;
    --ink: #2a2a2a;
    --muted: #4a4a4a;
    --blue: #1d6fb4;
    --bar-blue: #4a8fd8;
    --bar-dark: #26394a;
    --bar-cyan: #27c3f3;
    --canvas: #f3f3f3;
    --border: #d6d6d6;
    --app-red: #c9472b;
    --menubar: #ececec;
    --ribbon: #f6f6f6;
    --ui-text: #333;
    --ui-muted: #8a8a8a;
    --icon: #c4c4c4;
  }
  * { box-sizing: border-box; margin: 0; padding: 0; }
  html, body { width: 1200px; height: 675px; overflow: hidden; }
  body { background: var(--canvas); font-family: "Open Sans", sans-serif; color: var(--ink); position: relative; }

  /* ---------- application chrome ---------- */
  .menubar { position: absolute; left: 0; top: 0; width: 1200px; height: 14px; background: var(--menubar); font-size: 8.5px; color: #111; }
  .menubar span, .titlebar span, .tabs span, .ribbon .lbl, .statusbar span { position: absolute; white-space: nowrap; }
  .menubar span { top: 1px; }
  .menubar .app { font-weight: 700; }
  .titlebar { position: absolute; left: 0; top: 14px; width: 1200px; height: 16px; background: var(--app-red); color: var(--white); font-size: 8px; }
  .light { position: absolute; top: 4px; width: 7px; height: 7px; border-radius: 50%; }
  .search { position: absolute; left: 1034px; top: 2px; width: 132px; height: 12px; background: rgba(255,255,255,.18); border-radius: 2px; font-size: 7px; padding: 1px 0 0 16px; color: rgba(255,255,255,.8); }
  .tabs { position: absolute; left: 0; top: 30px; width: 1200px; height: 16px; background: var(--app-red); color: var(--white); font-size: 8px; }
  .tabs span { top: 3px; }
  .tabs .active { top: 2px; left: 8px; width: 36px; height: 14px; background: var(--ribbon); color: var(--app-red); font-weight: 600; text-align: center; padding-top: 1px; border-radius: 2px 2px 0 0; }
  .ribbon { position: absolute; left: 0; top: 46px; width: 1200px; height: 45px; background: var(--ribbon); border-bottom: 1px solid #ddd; font-size: 6.4px; color: var(--ui-text); }
  .ribbon .lbl { line-height: 1.1; text-align: center; }
  .ribbon .lbl.dim { color: var(--ui-muted); }
  .ico { position: absolute; background: var(--icon); border-radius: 1px; }
  .field { position: absolute; height: 13px; border: 1px solid #d3d3d3; background: #fff; font-size: 6.8px; color: var(--ui-muted); padding: 1px 3px; }
  .sep { position: absolute; top: 4px; width: 1px; height: 38px; background: #dedede; }
  .statusbar { position: absolute; left: 0; top: 661px; width: 1200px; height: 14px; background: #ececec; border-top: 1px solid #d8d8d8; font-size: 7.5px; color: var(--ui-text); }
  .statusbar span { top: 1px; }
  .zoom { position: absolute; left: 1036px; top: 6px; width: 80px; height: 1px; background: #999; }
  .zoom::after { content: ""; position: absolute; left: 46px; top: -3px; width: 7px; height: 7px; border-radius: 50%; background: #fff; border: 1px solid #888; }

  /* ---------- slide sorter ---------- */
  .sorter { position: absolute; left: 11px; top: 97px; display: grid; grid-template-columns: repeat(5, 223px); column-gap: 13.5px; grid-auto-rows: 149px; }
  .cell { position: relative; }
  .slide { position: relative; width: 216px; height: 122px; background: var(--white); border: 1px solid var(--border); overflow: hidden; transform: scale(1.0324); transform-origin: 0 0; }
  .slide--green { background: var(--green); color: var(--white); }
  .slide-number { position: absolute; left: 1px; top: 132px; font-size: 7px; color: #666; }
  .insert-mark { position: absolute; left: 947px; top: 389px; width: 1px; height: 135px; background: #e08a80; }
  .el { position: absolute; }
  .brand { display: flex; align-items: center; gap: 2px; font-weight: 700; color: var(--blue); white-space: nowrap; }
  .slide--green .brand { color: var(--white); }
  .brand__dot { border-radius: 50%; background: currentColor; }
  .brand--lg { font-size: 4px; }
  .brand--lg .brand__dot { width: 8px; height: 8px; }
  .brand--sm { font-size: 2.6px; }
  .brand--sm .brand__dot { width: 5px; height: 5px; }
  .drop { position: absolute; border-radius: 50%; background: var(--blue); opacity: .12; }
  .slide--green .drop { background: #3f8a2a; opacity: .35; }
  .title { font-weight: 700; white-space: nowrap; }
  .title--lg { font-size: 8.4px; }
  .title--md { font-size: 8px; }
  .title--xs { font-size: 3.6px; }
  .meta { font-size: 3px; }
  .date { font-size: 1.8px; color: var(--muted); }
  .slide--green .date, .slide--green .meta { color: var(--white); }
  .body { font-size: 3.1px; line-height: 1.6; color: var(--muted); }
  .slide--green .body { color: var(--white); }
  .body--link { text-decoration: underline; color: var(--ink); font-size: 2.3px; line-height: 1.5; }
  .slide--green .body--link { color: var(--white); }
  .bullets { list-style: none; font-size: 2.6px; line-height: 3.4; }
  .bullets li::before { content: "– "; }
  .photo { position: absolute; }
  .photo--hiker { background: linear-gradient(135deg, #d9c9ae, #c58a3a 45%, #6d5b48); }
  .photo--flowers { background: linear-gradient(135deg, #a08c78, #6f7a55 50%, #b79bc4); }
  .photo--meeting { background: linear-gradient(135deg, #e9eff3, #9fb7c9 50%, #4f7f5a); }
  .chart { position: absolute; }
</style>
</head>
<body>

<header class="menubar">
  <span class="app" style="left:34px">Slides</span>
  <span style="left:94px">File</span><span style="left:120px">Edit</span><span style="left:147px">View</span>
  <span style="left:178px">Insert</span><span style="left:213px">Format</span><span style="left:253px">Arrange</span>
  <span style="left:297px">Tools</span><span style="left:330px">Slide Show</span><span style="left:386px">Window</span>
  <span style="left:430px">Help</span>
  <span style="left:999px">Wed 4:48:18 PM</span><span style="left:1097px">Dana Reyes</span>
</header>

<div class="titlebar">
  <i class="light" style="left:8px;background:#fc605c"></i>
  <i class="light" style="left:20px;background:#fdbc40"></i>
  <i class="light" style="left:32px;background:#34c84a"></i>
  <span style="left:575px;top:2px">Corvanta_FA-V1</span>
  <div class="search">Search in Presentation</div>
</div>

<nav class="tabs">
  <span class="active">Home</span>
  <span style="left:53px">Insert</span><span style="left:92px">Design</span><span style="left:136px">Transitions</span>
  <span style="left:195px">Animations</span><span style="left:255px">Slide Show</span><span style="left:314px">Review</span>
  <span style="left:358px">View</span><span style="left:393px">Exporter</span>
  <span style="left:1150px">Share</span>
</nav>

<div class="ribbon">
  <i class="ico" style="left:10px;top:5px;width:14px;height:18px"></i><span class="lbl dim" style="left:11px;top:26px">Paste</span>
  <i class="ico" style="left:43px;top:5px;width:7px;height:6px"></i><span class="lbl dim" style="left:54px;top:4px">Cut</span>
  <i class="ico" style="left:43px;top:18px;width:7px;height:6px"></i><span class="lbl dim" style="left:54px;top:17px">Copy</span>
  <i class="ico" style="left:43px;top:32px;width:7px;height:6px"></i><span class="lbl dim" style="left:54px;top:31px">Format</span>
  <i class="ico" style="left:94px;top:5px;width:18px;height:17px"></i><span class="lbl" style="left:97px;top:26px">New<br>Slide</span>
  <i class="ico" style="left:127px;top:5px;width:9px;height:6px"></i><span class="lbl dim" style="left:140px;top:4px">Layout</span>
  <i class="ico" style="left:127px;top:18px;width:9px;height:6px"></i><span class="lbl dim" style="left:140px;top:17px">Reset</span>
  <i class="ico" style="left:127px;top:32px;width:9px;height:6px"></i><span class="lbl" style="left:140px;top:31px">Section</span>
  <div class="field" style="left:182px;top:5px;width:90px">Source Sans Pro</div>
  <div class="field" style="left:275px;top:5px;width:28px">9</div>
  <i class="ico" style="left:308px;top:6px;width:32px;height:11px"></i><i class="ico" style="left:346px;top:6px;width:18px;height:11px"></i>
  <i class="ico" style="left:184px;top:25px;width:176px;height:11px;opacity:.6"></i>
  <i class="sep" style="left:369px"></i>
  <i class="ico" style="left:375px;top:6px;width:140px;height:11px;opacity:.6"></i>
  <i class="ico" style="left:375px;top:25px;width:120px;height:11px;opacity:.6"></i>
  <i class="ico" style="left:523px;top:6px;width:20px;height:14px"></i><span class="lbl dim" style="left:517px;top:26px">Convert to<br>SmartArt</span>
  <i class="sep" style="left:558px"></i>
  <i class="ico" style="left:566px;top:6px;width:18px;height:14px"></i><span class="lbl dim" style="left:566px;top:26px">Picture</span>
  <i class="ico" style="left:600px;top:6px;width:16px;height:14px"></i><span class="lbl dim" style="left:597px;top:26px">Shapes</span>
  <i class="ico" style="left:630px;top:6px;width:16px;height:14px"></i><span class="lbl dim" style="left:631px;top:26px">Text<br>Box</span>
  <i class="sep" style="left:656px"></i>
  <i class="ico" style="left:665px;top:6px;width:18px;height:14px"></i><span class="lbl dim" style="left:663px;top:26px">Arrange</span>
  <i class="ico" style="left:697px;top:6px;width:18px;height:14px"></i><span class="lbl dim" style="left:697px;top:26px">Quick<br>Styles</span>
  <i class="ico" style="left:731px;top:5px;width:8px;height:7px"></i><span class="lbl dim" style="left:743px;top:4px">Shape Fill</span>
  <i class="ico" style="left:731px;top:24px;width:8px;height:7px"></i><span class="lbl dim" style="left:743px;top:23px">Shape Outline</span>
  <i class="sep" style="left:801px"></i>
  <i class="ico" style="left:828px;top:5px;width:14px;height:17px"></i><span class="lbl" style="left:808px;top:26px">Create and Share<br>Docu PDF</span>
</div>

<main class="sorter">

  <div class="cell"><section class="slide">
    <div class="el brand brand--lg" style="left:12px;top:14px"><span class="brand__dot"></span>Corvanta Energy</div>
    <h2 class="el title title--lg" style="left:11px;top:52px">What is Lorem Ipsum?</h2>
    <p class="el meta" style="left:11px;top:70px">What is Lorem Ipsum?</p>
    <p class="el meta" style="left:11px;top:96px"><b>Date:</b> July, 22, 2020</p>
    <div class="drop" style="right:-10px;bottom:-10px;width:50px;height:50px"></div>
  </section><span class="slide-number">1</span></div>

  <div class="cell"><section class="slide slide--green">
    <div class="el brand brand--lg" style="left:12px;top:14px"><span class="brand__dot"></span>Corvanta Energy</div>
    <h2 class="el title title--lg" style="left:11px;top:47px">What is Lorem Ipsum?</h2>
    <p class="el meta" style="left:11px;top:66px">What is Lorem Ipsum?</p>
    <p class="el meta" style="left:11px;top:96px"><b>Date:</b> July 22, 2020</p>
    <div class="drop" style="right:-10px;bottom:-10px;width:50px;height:50px"></div>
  </section><span class="slide-number">2</span></div>

  <div class="cell"><section class="slide">
    <div class="el brand brand--lg" style="left:12px;top:14px"><span class="brand__dot"></span>Corvanta Energy</div>
    <h2 class="el title title--lg" style="left:11px;top:47px">What is Lorem Ipsum?</h2>
    <p class="el meta" style="left:11px;top:66px">What is Lorem Ipsum?</p>
    <div class="drop" style="right:-10px;bottom:-10px;width:50px;height:50px"></div>
  </section><span class="slide-number">3</span></div>

  <div class="cell"><section class="slide slide--green">
    <div class="el brand brand--lg" style="left:12px;top:14px"><span class="brand__dot"></span>Corvanta Energy</div>
    <h2 class="el title title--lg" style="left:11px;top:47px">What is Lorem Ipsum?</h2>
    <p class="el meta" style="left:11px;top:66px">What is Lorem Ipsum?</p>
    <div class="drop" style="right:-10px;bottom:-10px;width:50px;height:50px"></div>
  </section><span class="slide-number">4</span></div>

  <div class="cell"><section class="slide">
    <p class="el date" style="left:8px;top:8px">July 22, 2020</p>
    <div class="el brand brand--sm" style="right:8px;top:9px"><span class="brand__dot"></span>Corvanta Energy</div>
    <h2 class="el title title--md" style="left:8px;top:25px">What is Lorem Ipsum?</h2>
    <p class="el body body--link" style="left:8px;top:38px;width:190px">Lorem Ipsum is simply dummy text of the printing and typesetting industry. Lorem Ipsum has been the industry's standard dummy text ever since the 1500s, when an unknown printer took a galley of type and scrambled it to make a type specimen book. Lorem Ipsum is simply dummy text of the printing and typesetting industry. Lorem Ipsum has been the industry's standard dummy text ever since the 1500s.<br>Lorem Ipsum is simply dummy text of the printing and typesetting industry. Lorem Ipsum has been the industry's standard dummy text ever since the 1500s, when an unknown printer took a galley of type and scrambled it to make a type specimen book.</p>
    <div class="drop" style="left:-8px;bottom:-8px;width:34px;height:34px"></div>
  </section><span class="slide-number">5</span></div>

  <div class="cell"><section class="slide slide--green">
    <p class="el date" style="left:8px;top:8px">July 22, 2020</p>
    <div class="el brand brand--sm" style="right:8px;top:9px"><span class="brand__dot"></span>Corvanta Energy</div>
    <h2 class="el title title--md" style="left:8px;top:25px">Click here to add title</h2>
    <p class="el body body--link" style="left:8px;top:38px;width:196px">Lorem Ipsum is simply dummy text of the printing and typesetting industry. Lorem Ipsum has been the industry's standard dummy text ever since the 1500s, when an unknown printer took a galley of type and scrambled it to make a type specimen book. Lorem Ipsum is simply dummy text of the printing and typesetting industry.<br>Lorem Ipsum is simply dummy text of the printing and typesetting industry. Lorem Ipsum has been the industry's standard dummy text ever since the 1500s, when an unknown printer took a galley of type and scrambled it to make a type specimen book.</p>
    <div class="drop" style="left:-8px;bottom:-8px;width:34px;height:34px"></div>
  </section><span class="slide-number">6</span></div>

  <div class="cell"><section class="slide">
    <p class="el date" style="left:8px;top:8px">July 22, 2020</p>
    <div class="el brand brand--sm" style="right:8px;top:9px"><span class="brand__dot"></span>Corvanta Energy</div>
    <p class="el body body--link" style="left:8px;top:28px;width:66px">Lorem Ipsum is simply dummy text of the printing and typesetting industry. Lorem Ipsum has been the industry's standard dummy text ever since the 1500s, when an unknown printer took a galley of type and scrambled it to make a type specimen book. It has survived not only five centuries, but also the leap into electronic typesetting, remaining essentially unchanged.</p>
    <p class="el body" style="left:106px;top:28px;width:94px">Lorem Ipsum is simply dummy text of the printing and typesetting industry. Lorem Ipsum has been the industry's standard dummy text ever since the 1500s, when an unknown printer took a galley of type and scrambled it to make a type specimen book.</p>
    <h2 class="el title title--md" style="left:106px;top:100px">What is Lorem Ipsum?</h2>
    <div class="drop" style="left:-8px;bottom:-8px;width:34px;height:34px"></div>
  </section><span class="slide-number">7</span></div>

  <div class="cell"><section class="slide slide--green">
    <p class="el date" style="left:8px;top:8px">July 22, 2020</p>
    <div class="el brand brand--sm" style="right:8px;top:9px"><span class="brand__dot"></span>Corvanta Energy</div>
    <p class="el body body--link" style="left:8px;top:28px;width:66px">Lorem Ipsum is simply dummy text of the printing and typesetting industry. Lorem Ipsum has been the industry's standard dummy text ever since the 1500s, when an unknown printer took a galley of type and scrambled it to make a type specimen book.</p>
    <p class="el body" style="left:106px;top:28px;width:94px">Lorem Ipsum is simply dummy text of the printing and typesetting industry. Lorem Ipsum has been the industry's standard dummy text ever since the 1500s, when an unknown printer took a galley of type and scrambled it to make a type specimen book. It has survived not only five centuries, but also the leap into electronic typesetting, remaining essentially unchanged.</p>
    <h2 class="el title title--md" style="left:106px;top:100px">Click here to add title</h2>
    <div class="drop" style="left:-8px;bottom:-8px;width:34px;height:34px"></div>
  </section><span class="slide-number">8</span></div>

  <div class="cell"><section class="slide">
    <p class="el date" style="left:8px;top:8px">July 22, 2020</p>
    <div class="el brand brand--sm" style="right:8px;top:9px"><span class="brand__dot"></span>Corvanta Energy</div>
    <p class="el body" style="left:8px;top:28px;width:86px">Lorem Ipsum is simply dummy text of the printing and typesetting industry. Lorem Ipsum has been the industry's standard dummy text ever since the 1500s, when an unknown printer took a galley of type and scrambled it to make a type specimen book.</p>
    <div class="photo photo--meeting" role="img" aria-label="Photo of two people reviewing plans at a desk" style="left:106px;top:27px;width:97px;height:69px"></div>
    <h2 class="el title title--md" style="left:106px;top:100px">What is Lorem Ipsum?</h2>
    <div class="drop" style="left:-8px;bottom:-8px;width:34px;height:34px"></div>
  </section><span class="slide-number">9</span></div>

  <div class="cell"><section class="slide slide--green">
    <p class="el date" style="left:8px;top:8px">July 22, 2020</p>
    <div class="el brand brand--sm" style="right:8px;top:9px"><span class="brand__dot"></span>Corvanta Energy</div>
    <p class="el body" style="left:8px;top:28px;width:86px">Lorem Ipsum is simply dummy text of the printing and typesetting industry. Lorem Ipsum has been the industry's standard dummy text ever since the 1500s, when an unknown printer took a galley of type and scrambled it to make a type specimen book.</p>
    <div class="photo photo--meeting" role="img" aria-label="Photo of two people reviewing plans at a desk" style="left:106px;top:27px;width:97px;height:69px"></div>
    <h2 class="el title title--md" style="left:106px;top:100px">What is Lorem Ipsum?</h2>
    <div class="drop" style="left:-8px;bottom:-8px;width:34px;height:34px"></div>
  </section><span class="slide-number">10</span></div>

  <div class="cell"><section class="slide">
    <p class="el date" style="left:8px;top:8px">July 22, 2020</p>
    <div class="el brand brand--sm" style="right:8px;top:9px"><span class="brand__dot"></span>Corvanta Energy</div>
    <div class="photo photo--hiker" role="img" aria-label="Photo of a hiker with a backpack outdoors" style="left:8px;top:28px;width:98px;height:70px"></div>
    <div class="photo photo--flowers" role="img" aria-label="Photo of a flowering plant in a pot" style="left:107px;top:28px;width:97px;height:70px"></div>
  </section><span class="slide-number">11</span></div>

  <div class="cell"><section class="slide slide--green">
    <p class="el date" style="left:8px;top:8px">July 22, 2020</p>
    <div class="el brand brand--sm" style="right:8px;top:9px"><span class="brand__dot"></span>Corvanta Energy</div>
    <div class="photo photo--hiker" role="img" aria-label="Photo of a hiker with a backpack outdoors" style="left:8px;top:28px;width:98px;height:70px"></div>
    <div class="photo photo--flowers" role="img" aria-label="Photo of a flowering plant in a pot" style="left:107px;top:28px;width:97px;height:70px"></div>
  </section><span class="slide-number">12</span></div>

  <div class="cell"><section class="slide">
    <p class="el date" style="left:8px;top:8px">July 22, 2020</p>
    <div class="el brand brand--sm" style="right:8px;top:9px"><span class="brand__dot"></span>Corvanta Energy</div>
    <h3 class="el title title--xs" style="left:8px;top:29px">What is Lorem Ipsum?</h3>
    <ul class="el bullets" style="left:8px;top:40px"><li>Bullets 1</li><li>Bullets 2</li><li>Bullets 3</li></ul>
    <svg class="chart" style="left:108px;top:26px" width="96" height="66" viewBox="0 0 96 66">
      <g stroke="#e3e3e3" stroke-width=".4"><line x1="4" y1="6" x2="94" y2="6"/><line x1="4" y1="20" x2="94" y2="20"/><line x1="4" y1="34" x2="94" y2="34"/><line x1="4" y1="48" x2="94" y2="48"/><line x1="4" y1="60" x2="94" y2="60"/></g>
      <rect x="8" y="18" width="4" height="42" fill="var(--bar-blue)"/><rect x="13" y="37" width="4" height="23" fill="var(--bar-dark)"/><rect x="18" y="42" width="4" height="18" fill="var(--bar-cyan)"/>
      <rect x="30" y="30" width="4" height="30" fill="var(--bar-blue)"/><rect x="35" y="14" width="4" height="46" fill="var(--bar-dark)"/><rect x="40" y="42" width="4" height="18" fill="var(--bar-cyan)"/>
      <rect x="52" y="24" width="4" height="36" fill="var(--bar-blue)"/><rect x="57" y="44" width="4" height="16" fill="var(--bar-dark)"/><rect x="62" y="34" width="4" height="26" fill="var(--bar-cyan)"/>
      <rect x="74" y="12" width="4" height="48" fill="var(--bar-blue)"/><rect x="79" y="28" width="4" height="32" fill="var(--bar-dark)"/><rect x="84" y="4" width="4" height="56" fill="var(--bar-cyan)"/>
      <g font-size="1.8" fill="#888" font-family="Open Sans, sans-serif"><text x="8" y="64">Category 1</text><text x="30" y="64">Category 2</text><text x="52" y="64">Category 3</text><text x="74" y="64">Category 4</text></g>
    </svg>
    <h2 class="el title title--md" style="left:108px;top:100px">What is Lorem Ipsum?</h2>
    <div class="drop" style="left:-8px;bottom:-8px;width:34px;height:34px"></div>
  </section><span class="slide-number">13</span></div>

  <div class="cell"><section class="slide slide--green">
    <p class="el date" style="left:8px;top:8px">July 22, 2020</p>
    <div class="el brand brand--sm" style="right:8px;top:9px"><span class="brand__dot"></span>Corvanta Energy</div>
    <h3 class="el title title--xs" style="left:8px;top:29px">What is Lorem Ipsum?</h3>
    <ul class="el bullets" style="left:8px;top:40px"><li>Bullets 1</li><li>Bullets 2</li><li>Bullets 3</li></ul>
    <svg class="chart" style="left:108px;top:26px" width="96" height="66" viewBox="0 0 96 66">
      <rect x="8" y="18" width="4" height="42" fill="var(--bar-blue)"/><rect x="13" y="37" width="4" height="23" fill="var(--bar-dark)"/><rect x="18" y="42" width="4" height="18" fill="var(--bar-cyan)"/>
      <rect x="30" y="30" width="4" height="30" fill="var(--bar-blue)"/><rect x="35" y="14" width="4" height="46" fill="var(--bar-dark)"/><rect x="40" y="42" width="4" height="18" fill="var(--bar-cyan)"/>
      <rect x="52" y="24" width="4" height="36" fill="var(--bar-blue)"/><rect x="57" y="44" width="4" height="16" fill="var(--bar-dark)"/><rect x="62" y="34" width="4" height="26" fill="var(--bar-cyan)"/>
      <rect x="74" y="12" width="4" height="48" fill="var(--bar-blue)"/><rect x="79" y="28" width="4" height="32" fill="var(--bar-dark)"/><rect x="84" y="4" width="4" height="56" fill="var(--bar-cyan)"/>
      <g font-size="1.8" fill="#ffffff" font-family="Open Sans, sans-serif"><text x="8" y="64">Category 1</text><text x="30" y="64">Category 2</text><text x="52" y="64">Category 3</text><text x="74" y="64">Category 4</text></g>
    </svg>
    <h2 class="el title title--md" style="left:108px;top:100px">What is Lorem Ipsum?</h2>
    <div class="drop" style="left:-8px;bottom:-8px;width:34px;height:34px"></div>
  </section><span class="slide-number">14</span></div>

</main>
<i class="insert-mark"></i>

<footer class="statusbar">
  <span style="left:16px">Slide 1 of 14</span>
  <span style="left:72px">English (United States)</span>
  <i class="zoom"></i>
  <span style="left:1136px">147%</span>
</footer>

</body>
</html>
```